Business Cards and Stationery - Real Estate
See "information" and "additional comments"
Business Cards and Stationery - Real Estate - Real Estate
Creative Brief
Professional
Anselm Varga
Managing Broker
4382 SW Route 14, Ste 305 Vancouver, WA 98671
Direct - 360-555-0147
Cell - 360-555-0193
anselm@fernloftpm.example
www.fernlofthomes.example
Licensed in OR & WA
We want to use UV spotting on our cards. Here is a video link from the printing company we are using. If you are unfamiliar with creating files for UV spotting, it requires one file for the card and a second mask file for the UV spotting. https://www.clipvault.example/watch?v=Qx7rLm2PzA1 I've uploaded the template files to use from Zentra Print along with our Adobe Illustrator Logo files and a head shot. We probably don't want a head shot on the card, but have uploaded just in case. Please use Adobe Illustrator.
Probably just the logo. Something that is clean, possible a repeated design such as the logo. Would like to consider UV spotting on back. Try searching for "business cards spot uv" on Google, then look at the "images" link.
SiteAdmin SiteAdmin
Dear Designers, Kindly follow the below mention instructions by the Project holder for better and improve designs: We want to use spot UV on our cards, front and back. Here is a video Link from the printing company we are using. If you are unfamiliar with creating file for Spot UV, it requires one file for the card and a second mask file for the UV spotting. https://www.clipvault.example/watch?v=Qx7rLm2PzA1 Use your creativity, but a couple ideas for the back would be to repeat our logo over and over across the entire back. It may be nice to somehow put our website within those repeated logos. Or it may not be nice, depending on how it looks. You could also just make our logo with URL on the back. For the front, you will have to be creative to make it work. Our logo could be UV spotted. And then probably some sort of nice design that covers a portion of the front, keeping in mind that the uv spot coating design can overlap anything. Or maybe it would look best to only spot uv our logo. The content for the card is in our creative brief. We would also like to include "We Love Referrals!" somewhere on the card. Here are a few images for some ideas. Keep in mind that we don't want a copy of what is done with these ideas. They are simply ideas of what can be done with UV spotting. https://pressglow.example/assets/images/gallery/business-cards/images/a1b2c3d4e5f60718293a4b5c6d7e8f90.png https://pressglow.example/assets/uploads/spot_uv_marlow_business_cards.jpg http://media.shopweave.example/51730264/Renata-Pell-spot-gloss-silver-foil-spot-uv-silk-unique-cool-business-cards_full.jpeg http://www.quartzlinecards.example/images/img-gallery/silk-business-card-with-spot-uv-harrow-cellars.jpg http://i01.i.tradepix.example/wsphoto/v2/813406572_2/Custom-Spot-UV-business-card-matt-coated-paper-350gsm-High-quality.jpg http://www.newswire.example/64028195-silk-laminated-business-cards-with-spot-uv.jpg http://www.atelier-cartes-nord.example/wp-content/uploads/2010/10/carte-commerciale-vernis-selectif.jpg https://pressglow.example/assets/uploads/spot_uv_cards_dravetek.jpg http://www.calloutmailers.example/wp/wp-content/uploads/2013/03/zebra-orange-spot-uv-business-card1.png http://layoutharbor.example/wp-content/uploads/2013/04/square-business-card-29.jpg
fernloft47 fernloft47
I forgot to add on that last comment, that the black designs are way to dark for our tastes. Blue on the back looks nice. We prefer the lighter designs on the front of the card.
We are looking for double sided cards with rounded corners and some UV spotting on both sides. We like the design of #96 on the back side, however it looks like there may be some silver foil on the logo. We won't be doing foil, just spotting. There are a lot of nice designs so far, but we need to have the combination of rounded corners and UV spotting. Thanks.

```html
<!DOCTYPE html>
<html lang="en">
<head>
<meta charset="utf-8">
<title>Fernloft Business Cards</title>
<link href="https://fonts.googleapis.com/css2?family=Montserrat:wght@400;600;700&display=swap" rel="stylesheet">
<style>
  :root {
    --bg: #e9eaec;
    --card: #ffffff;
    --blue: #1f4f9c;
    --blue-deep: #163d7c;
    --blue-soft: #c9d6ea;
    --ink: #3a3f48;
    --ink-soft: #6b717c;
  }
  * { margin: 0; padding: 0; box-sizing: border-box; }
  html, body { width: 1200px; height: 828px; overflow: hidden; }
  body {
    background: var(--bg);
    font-family: "Montserrat", sans-serif;
    position: relative;
  }
  .card {
    position: absolute;
    top: 266px;
    width: 520px;
    height: 297px;
    background: var(--card);
    border-radius: 14px;
    overflow: hidden;
    box-shadow: 0 6px 18px rgba(0,0,0,0.12);
  }
  .card--back { left: 60px; }
  .card--front { left: 620px; }
  .card svg.swoosh { position: absolute; inset: 0; width: 100%; height: 100%; }

  .brand { position: absolute; display: flex; align-items: center; gap: 10px; }
  .brand__square { width: 22px; height: 22px; background: var(--blue); border-radius: 3px; }
  .brand__name { font-weight: 700; color: var(--blue); letter-spacing: 2px; }
  .brand__tag { position: absolute; font-size: 7px; letter-spacing: 3px; color: var(--ink-soft); font-weight: 600; }

  .card--back .brand { left: 58px; top: 128px; }
  .card--back .brand__square { width: 34px; height: 34px; }
  .card--back .brand__name { font-size: 26px; }

  .card--front .brand { left: 28px; top: 248px; }
  .card--front .brand__name { font-size: 17px; }
  .card--front .brand__tag { left: 60px; top: 270px; }

  .contact { position: absolute; right: 28px; top: 30px; text-align: right; color: var(--ink); }
  .contact__name { font-size: 15px; font-weight: 700; color: var(--blue); letter-spacing: 1.5px; text-transform: uppercase; }
  .contact__role { font-size: 9px; font-weight: 600; letter-spacing: 2px; text-transform: uppercase; color: var(--ink-soft); margin-top: 3px; }
  .contact__address { font-size: 8.5px; line-height: 1.5; margin-top: 18px; }
  .contact__lines { list-style: none; font-size: 8.5px; line-height: 1.7; margin-top: 12px; }
  .contact__lines li { display: flex; justify-content: flex-end; align-items: center; gap: 6px; }
  .contact__lines .dot { width: 6px; height: 6px; background: var(--blue); border-radius: 50%; }
</style>
</head>
<body>

<section class="card card--back" aria-label="Card back">
  <svg class="swoosh" viewBox="0 0 520 297" aria-hidden="true">
    <path d="M250,0 C360,30 450,70 520,150 L520,0 Z" fill="var(--blue-soft)"/>
    <path d="M300,0 C390,25 470,70 520,120 L520,0 Z" fill="var(--blue)"/>
    <path d="M230,0 C340,35 440,85 520,175" fill="none" stroke="var(--blue-soft)" stroke-width="2"/>
  </svg>
  <div class="brand">
    <span class="brand__square"></span>
    <span class="brand__name">FERNLOFT</span>
  </div>
</section>

<section class="card card--front" aria-label="Card front">
  <svg class="swoosh" viewBox="0 0 520 297" aria-hidden="true">
    <path d="M0,0 L170,0 C250,80 290,190 350,297 L0,297 Z" fill="var(--blue)"/>
    <path d="M0,0 L120,0 C200,90 230,180 260,297 L0,297 Z" fill="var(--blue-deep)" opacity="0.35"/>
    <path d="M0,205 C130,195 250,235 330,297 L0,297 Z" fill="var(--card)"/>
    <path d="M0,198 C130,188 255,228 340,297" fill="none" stroke="var(--blue-soft)" stroke-width="3"/>
    <path d="M185,0 C265,85 305,195 365,297" fill="none" stroke="var(--blue-soft)" stroke-width="2"/>
  </svg>

  <div class="contact">
    <p class="contact__name">Anselm Varga</p>
    <p class="contact__role">Managing Broker</p>
    <p class="contact__address">4382 SW Route 14, Ste 305<br>Vancouver, WA 98671</p>
    <ul class="contact__lines">
      <li>Direct 360-555-0147 <span class="dot"></span></li>
      <li>Cell 360-555-0193 <span class="dot"></span></li>
      <li>anselm@fernloftpm.example <span class="dot"></span></li>
      <li>www.fernlofthomes.example <span class="dot"></span></li>
    </ul>
  </div>

  <div class="brand">
    <span class="brand__square"></span>
    <span class="brand__name">FERNLOFT</span>
  </div>
  <span class="brand__tag">PROPERTIES</span>
</section>

</body>
</html>
```